Stationery Design Project

We are interested in A4 paper letterheads, envelopes, maybe A4 folders where we can put the patients' results in and businesscards. No information will be given out for the time being.
We would like to see mainly shades of white.. please refer to
http://en.huevaultix.org/wiki/Category:Shades_of_white
anti-flash white, splashed white,ghost white, ivory, snow and white smoke or even light grey
we are interested mainly on the silver design but we welcome the other colors as well. Since its about a gynecologist please avoid dark colors, instead use shades of beige, light grey and white

```html
<!DOCTYPE html>
<html lang="en">
<head>
<meta charset="utf-8">
<title>Stationery Set – Letterhead, Envelope, Business Cards</title>
<link rel="stylesheet" href="https://fonts.googleapis.com/css2?family=Roboto:wght@300;400;700&display=swap">
<style>
  :root {
    --backdrop: #e4e4e6;
    --paper: #ffffff;
    --paper-shade: #f6f6f6;
    --beige: #e8dab8;
    --beige-light: #f4ecda;
    --tan: #d5b98a;
    --ink: #222222;
    --ink-soft: #7a7a7a;
    --ink-faint: #a8a8a8;
    --window: #f1f1f1;
    --shadow: 0 6px 18px rgba(0,0,0,0.12);
  }
  * { box-sizing: border-box; margin: 0; padding: 0; }
  html, body {
    width: 1200px; height: 900px; overflow: hidden;
    background: var(--backdrop);
    font-family: "Roboto", Arial, sans-serif;
  }
  .canvas { position: relative; width: 1200px; height: 900px; }

  /* brand line (name beside a plain circle) */
  .brand { display: flex; align-items: center; gap: 10px; }
  .brand-circle {
    width: 30px; height: 30px; border-radius: 50%;
    border: 2px solid var(--tan); flex: none;
  }
  .brand-text { display: flex; flex-direction: column; }
  .brand-name { font-weight: 300; font-size: 17px; letter-spacing: 0.5px; color: var(--ink-soft); line-height: 1; }
  .brand-tagline { font-weight: 300; font-size: 6px; letter-spacing: 1px; color: var(--ink-faint); margin-top: 3px; }

  /* letterhead */
  .letterhead {
    position: absolute; left: 60px; top: 40px;
    width: 560px; height: 792px;
    background: var(--paper); box-shadow: var(--shadow);
    padding: 44px 50px;
  }
  .letter-body { margin-top: 80px; font-size: 8.6px; line-height: 1.75; color: var(--ink); }
  .letter-salutation { font-weight: 700; margin-bottom: 12px; }
  .letter-body p { margin-bottom: 12px; }

  /* envelopes */
  .envelope {
    position: absolute; width: 520px; height: 260px;
    background: var(--paper); box-shadow: var(--shadow); overflow: hidden;
  }
  .envelope-back { left: 650px; top: 40px; }
  .envelope-front { left: 650px; top: 330px; padding: 40px 36px; }
  .envelope-band { position: absolute; left: 0; top: 0; width: 100%; height: 110px; }
  .envelope-window {
    position: absolute; right: 34px; bottom: 52px;
    width: 210px; height: 88px; border-radius: 10px;
    background: var(--window); border: 1px solid #e2e2e2;
  }

  /* business cards */
  .card {
    position: absolute; top: 640px; width: 250px; height: 162px;
    background: var(--beige); box-shadow: var(--shadow); overflow: hidden;
  }
  .card-front { left: 650px; }
  .card-back { left: 920px; }
  .card-wave { position: absolute; left: 0; bottom: 0; width: 100%; height: 50px; }
  .card-front .brand { position: absolute; left: 0; right: 0; top: 38px; justify-content: center; }
  .card-front .brand-circle { border-color: var(--paper); }
  .card-front .brand-name { color: var(--paper); }
  .card-url {
    position: absolute; left: 0; right: 0; top: 104px;
    text-align: center; font-size: 9px; font-weight: 300; letter-spacing: 0.6px; color: var(--paper);
  }
  .card-back .brand { position: absolute; left: 86px; top: 50px; }
  .card-back .brand-name { color: var(--ink-soft); font-size: 14px; }
  .card-contacts {
    position: absolute; left: 16px; right: 12px; bottom: 14px;
    display: flex; justify-content: space-between;
    font-size: 6px; font-weight: 300; color: var(--ink-soft); letter-spacing: 0.5px;
  }
</style>
</head>
<body>
<main class="canvas">

  <article class="letterhead">
    <header class="brand">
      <span class="brand-circle"></span>
      <span class="brand-text">
        <span class="brand-name">Xxxxx Xxxxxxxx</span>
        <span class="brand-tagline">xxxxxxxx xxxxxxxxx</span>
      </span>
    </header>
    <section class="letter-body">
      <p class="letter-salutation">Dear Customer,</p>
      <p>Lorem ipsum dolor sit amet, consectetur adipiscing elit. Donec elementum velit sit amet libero fringilla adipiscing. Aliquam sollicitudin, leo vitae molestie facilisis, tellus ligula varius velit, vitae tincidunt lacus purus vitae nulla. Nulla imperdiet, odio quis ultrices ornare, diam est dictum lacus, et vehicula est magna at metus. Integer mattis lorem quis tortor accumsan ultrices ac ut massa. Duis eget metus ut risus scelerisque ornare quis eget dui. Aliquam lobortis dolor vitae magna volutpat eu facilisis tellus molestie. Sed a purus quis nibh lacinia interdum ut at leo. Sed sem dui, mollis in pellentesque sed, placerat non erat. Cum sociis natoque penatibus et magnis dis parturient montes, nascetur ridiculus mus. In lacinia arcu non felis laoreet sed convallis lectus tincidunt. Duis quis mauris et enim egestas molestie vel id sem.</p>
      <p>Integer consequat velit quis elit hendrerit imperdiet. Donec felis velit, volutpat vel convallis nec, sollicitudin et nulla. Pellentesque sodales elementum aliquam. Donec convallis, turpis sit amet laoreet ultricies, enim est elementum magna, dictum lobortis eros tellus quis diam. Nunc suscipit augue non nisl volutpat volutpat. Ut egestas ultrices purus, eget varius nibh placerat in. Cras leo ante, congue id ultricies a, ornare eu est. Curabitur eleifend tincidunt mi eget tristique.</p>
      <p>Etiam arcu augue, ornare vitae consectetur luctus, tincidunt vitae urna. Lorem ipsum dolor sit amet, consectetur adipiscing elit. Donec vitae tortor quis orci adipiscing lobortis. Morbi aliquet orci quis mi viverra sollicitudin. Sed eget pellentesque turpis. Aliquam commodo sodales ultrices. Nullam ut elit vitae elit suscipit porttitor viverra non mi. Donec diam mi, tincidunt nec sodales vestibulum, iaculis a urna. Nulla facilisi. Integer consequat velit quis elit hendrerit imperdiet. Donec felis velit, volutpat vel convallis nec, sollicitudin et nulla. Pellentesque sodales elementum aliquam. Donec convallis, turpis sit amet laoreet ultricies.</p>
    </section>
  </article>

  <section class="envelope envelope-back">
    <svg class="envelope-band" viewBox="0 0 520 110" preserveAspectRatio="none" aria-hidden="true">
      <path d="M0 0 H520 V40 C380 30 180 70 0 110 Z" fill="var(--beige-light)"/>
      <path d="M0 0 H520 V22 C380 14 180 50 0 84 Z" fill="var(--beige)"/>
    </svg>
  </section>

  <section class="envelope envelope-front">
    <header class="brand">
      <span class="brand-circle"></span>
      <span class="brand-text">
        <span class="brand-name">Xxxxx Xxxxxxxx</span>
        <span class="brand-tagline">xxxxxxxx xxxxxxxxx</span>
      </span>
    </header>
    <div class="envelope-window"></div>
  </section>

  <section class="card card-front">
    <div class="brand">
      <span class="brand-circle"></span>
      <span class="brand-name">Xxxxx Xxxxxxxx</span>
    </div>
    <p class="card-url">www.xxxxxxxxxxxxxxxx.com</p>
    <svg class="card-wave" viewBox="0 0 250 50" preserveAspectRatio="none" aria-hidden="true">
      <path d="M0 30 C80 50 170 40 250 20 V50 H0 Z" fill="var(--beige-light)"/>
    </svg>
  </section>

  <section class="card card-back">
    <div class="brand">
      <span class="brand-text">
        <span class="brand-name">Xxxxx Xxxxxxxx</span>
        <span class="brand-tagline">xxxxxxxx xxxxxxxxx</span>
      </span>
    </div>
    <div class="card-contacts">
      <span>xxx xxxxx xxx xxxxx xx</span>
      <span>tel 55 555 55 55</span>
      <span>xxxxxx@xxxxxx.com</span>
    </div>
  </section>

</main>
</body>
</html>
```